New Invitation Design Project

We are looking for someone to design our e-vite, save the date and wine labels for our upcoming event on June 26th. Our event is an open house for our current clients and business colleagues to show our appreciation for them. We want to incorporate our new logo. We would like a professional but fun invitation with multiple versions in different manners of the design we choose.

Industry/Entity Type

House

```html
<!DOCTYPE html>
<html lang="en">
<head>
<meta charset="utf-8">
<title>KHM Open House Invitation</title>
<link href="https://fonts.googleapis.com/css2?family=Alfa+Slab+One&family=Archivo+Black&family=Oswald:wght@600&family=Ultra&family=Kaushan+Script&family=Roboto:wght@300;500&display=swap" rel="stylesheet">
<style>
  :root{
    --frame-dark:#2f5a5e;
    --frame-mid:#6f9a7c;
    --paper-light:#eef36a;
    --paper-mid:#d9e653;
    --paper-edge:#a9b93a;
    --blue:#1a7fd6;
    --blue-soft:#6a8fcf;
    --yellow:#f6d31a;
    --ink:#111111;
    --slate:#3d4a55;
    --grey:#4d4d4d;
    --rule:#9fa850;
    --web:#1d3f7a;
  }
  html,body{margin:0;padding:0;overflow:hidden;background:#ffffff;}
  .invite{
    position:relative;width:1200px;height:851px;box-sizing:border-box;
    border:14px solid var(--frame-dark);
    border-image:linear-gradient(135deg,var(--frame-mid),var(--frame-dark) 40%,#4f7a5a 70%,var(--frame-dark)) 1;
    background:radial-gradient(ellipse at 50% 45%,var(--paper-light) 0%,var(--paper-mid) 60%,var(--paper-edge) 100%);
    overflow:hidden;font-family:"Roboto",sans-serif;
  }
  .headline{
    position:absolute;top:28px;left:0;width:100%;text-align:center;margin:0;
    font-family:"Alfa Slab One",serif;font-size:38px;letter-spacing:2px;font-weight:400;
    color:var(--blue);-webkit-text-stroke:1px #0b2c55;
    text-shadow:0 0 12px rgba(255,255,255,.7);
  }
  .headline .accent{color:var(--yellow);-webkit-text-stroke:1px #7a5a00;}
  .feature-box{
    position:absolute;left:56px;top:104px;width:1062px;height:196px;
    border:3px dotted #333;box-sizing:border-box;
  }
  .firm-name{
    position:absolute;left:36px;top:58px;width:360px;
    display:flex;align-items:center;gap:14px;
    font-family:"Roboto",sans-serif;font-weight:500;font-size:34px;line-height:1.15;color:var(--slate);
  }
  .firm-name .mark{flex:none;width:22px;height:22px;background:var(--blue-soft);}
  .tagline{
    position:absolute;right:14px;top:14px;text-align:right;margin:0;
    font-family:"Oswald",sans-serif;font-weight:600;font-size:44px;line-height:61px;
    color:var(--blue-soft);letter-spacing:.5px;
  }
  .drink{
    position:absolute;top:362px;left:84px;display:flex;align-items:center;gap:14px;
    font-family:"Archivo Black",sans-serif;font-size:32px;color:var(--ink);
  }
  .drink svg{width:30px;height:30px;}
  .when{position:absolute;top:438px;left:50px;display:flex;gap:16px;
    font-family:"Ultra",serif;font-size:29px;color:var(--ink);}
  .when span{padding:6px 14px;background:rgba(255,255,235,.55);border-radius:10px;box-shadow:0 0 14px rgba(255,255,235,.8);}
  .badge{position:absolute;left:922px;top:318px;width:240px;height:190px;}
  .badge-text{
    position:absolute;left:922px;top:336px;width:240px;text-align:center;
    font-family:"Archivo Black",sans-serif;font-style:italic;font-size:34px;line-height:44px;color:#e8a400;
    -webkit-text-stroke:.6px #5a3a00;
  }
  .badge-text .dark{color:#5a2a10;}
  .rsvp{position:absolute;top:540px;left:50px;margin:0;
    font-family:"Kaushan Script",cursive;font-size:36px;color:var(--ink);letter-spacing:1px;}
  .rsvp .lead{color:var(--blue-soft);}
  .rule{position:absolute;left:50px;width:1072px;height:3px;background:var(--rule);}
  .contact{position:absolute;top:615px;margin:0;font-style:normal;
    font-family:"Roboto",sans-serif;font-weight:300;font-size:31px;line-height:43px;color:var(--grey);}
  .contact.left{left:46px;}
  .contact.right{right:64px;text-align:right;}
  .web{position:absolute;top:780px;left:0;width:100%;text-align:center;margin:0;
    font-family:"Roboto",sans-serif;font-size:32px;color:var(--web);letter-spacing:1px;}
</style>
</head>
<body>
<main class="invite">
  <h1 class="headline">YOU'RE INVITED TO THE KHM <span class="accent">OPEN HOUSE!</span></h1>

  <section class="feature-box">
    <div class="firm-name"><span class="mark"></span>Kessler Hart Moreno</div>
    <p class="tagline">MEET OUR NEWEST STAFF MEMBERS<br>AND ATTORNEYS NETWORK WITH<br>OUR FABULOUS GUESTS</p>
  </section>

  <div class="drink">
    <svg viewBox="0 0 24 24"><path d="M12 2l3 6.5 7 .8-5.2 4.8 1.4 7L12 17.6 5.8 21l1.4-7L2 9.3l7-.8z" fill="#e6d64a" stroke="#5a4a10" stroke-width="1.2"/></svg>
    <svg viewBox="0 0 24 24"><path d="M12 2l3 6.5 7 .8-5.2 4.8 1.4 7L12 17.6 5.8 21l1.4-7L2 9.3l7-.8z" fill="#e6d64a" stroke="#5a4a10" stroke-width="1.2"/></svg>
    <svg viewBox="0 0 24 24"><path d="M12 2l3 6.5 7 .8-5.2 4.8 1.4 7L12 17.6 5.8 21l1.4-7L2 9.3l7-.8z" fill="#e6d64a" stroke="#5a4a10" stroke-width="1.2"/></svg>
    <span>HAVE A DRINK ON US!</span>
    <svg viewBox="0 0 24 24"><path d="M12 2l3 6.5 7 .8-5.2 4.8 1.4 7L12 17.6 5.8 21l1.4-7L2 9.3l7-.8z" fill="#e6d64a" stroke="#5a4a10" stroke-width="1.2"/></svg>
    <svg viewBox="0 0 24 24"><path d="M12 2l3 6.5 7 .8-5.2 4.8 1.4 7L12 17.6 5.8 21l1.4-7L2 9.3l7-.8z" fill="#e6d64a" stroke="#5a4a10" stroke-width="1.2"/></svg>
    <svg viewBox="0 0 24 24"><path d="M12 2l3 6.5 7 .8-5.2 4.8 1.4 7L12 17.6 5.8 21l1.4-7L2 9.3l7-.8z" fill="#e6d64a" stroke="#5a4a10" stroke-width="1.2"/></svg>
  </div>

  <div class="when"><span>THURSDAY, JUNE 26, 2014</span><span>3:00PM - 7:00PM</span></div>

  <svg class="badge" viewBox="0 0 240 190">
    <defs>
      <radialGradient id="badgeFill" cx="45%" cy="35%" r="70%">
        <stop offset="0" stop-color="#fffbb0"/><stop offset=".6" stop-color="#f7ea3a"/><stop offset="1" stop-color="#d4b80a"/>
      </radialGradient>
    </defs>
    <path d="M20 40 Q120 -10 220 40 Q245 120 120 185 Q-5 120 20 40z" fill="url(#badgeFill)" stroke="#c9a80a" stroke-width="3"/>
  </svg>
  <div class="badge-text">DROP<br>BY<br>ANY<br><span class="dark">TIME!</span></div>

  <p class="rsvp"><span class="lead">RSVP</span> to mlowry@khmlegal.com or (847) 555-0142</p>

  <div class="rule" style="top:598px"></div>
  <address class="contact left">KESSLER, HART &amp; MORENO<br>ATTORNEYS AT LAW<br>847-555-0142</address>
  <address class="contact right">1820 BIRCHWOOD AVENUE<br>SUITE 210,<br>LAKEVIEW HEIGHTS, IL 60099</address>
  <div class="rule" style="top:766px"></div>

  <p class="web">WWW. KHMLEGAL.COM</p>
</main>
</body>
</html>
```